Vornel Technologies business card design

We need a business card designed with our new logo. it would be great if the card could communicate it is a technology based company.

Target Market(s)

system integrators

Industry/Entity Type

technology, IOT

Contact Information for Business Card

Name, designation, Address, telephone number, email address

Requirements
Must have
• logo and company name
Nice to have
• something to do with technology

```html
<!DOCTYPE html>
<html lang="en">
<head>
<meta charset="utf-8">
<title>Vornel Technologies Business Card</title>
<link rel="stylesheet" href="https://fonts.googleapis.com/css2?family=Fira+Sans:wght@400;600;700&display=swap">
<style>
  :root {
    --backdrop: #e4e4e4;
    --card-dark: #2b2a29;
    --accent: #f39420;
    --text-light: #f2f2f2;
    --pattern-light: #6a6a6a;
    --pattern-dark: #1a1a1a;
    --decor-brown: #3d3429;
    --decor-grey: #3a3a3a;
  }
  * { margin: 0; padding: 0; box-sizing: border-box; }
  html, body { width: 1200px; height: 960px; overflow: hidden; }
  body {
    background: var(--backdrop);
    font-family: "Fira Sans", Arial, sans-serif;
    position: relative;
  }
  .card {
    position: absolute;
    left: 298px;
    width: 607px;
    height: 347px;
    background: var(--card-dark);
    overflow: hidden;
  }
  .card-front { top: 114px; }
  .card-back { top: 515px; }

  .front-pattern {
    position: absolute;
    inset: 0;
    background: linear-gradient(100deg, var(--pattern-light) 0%, #3a3a3a 50%, var(--pattern-dark) 100%);
    opacity: 0.55;
  }
  .wordmark {
    position: absolute;
    display: flex;
    align-items: center;
    gap: 10px;
    font-weight: 600;
    color: var(--text-light);
    letter-spacing: 0.5px;
    white-space: nowrap;
  }
  .wordmark-square {
    width: 18px;
    height: 18px;
    background: var(--accent);
    flex: none;
  }
  .card-front .wordmark {
    left: 50%;
    top: 50%;
    transform: translate(-50%, -50%);
    font-size: 34px;
  }
  .card-back .wordmark {
    right: 44px;
    top: 52px;
    font-size: 27px;
  }

  .back-decoration {
    position: absolute;
    left: 0;
    top: 0;
    width: 300px;
    height: 347px;
    background: linear-gradient(160deg, var(--decor-brown) 0%, var(--decor-grey) 70%, var(--card-dark) 100%);
    opacity: 0.8;
    clip-path: polygon(0 0, 55% 0, 100% 40%, 70% 100%, 0 100%);
  }
  .name-marker {
    position: absolute;
    left: 0;
    top: 152px;
    width: 18px;
    height: 42px;
    background: var(--accent);
  }
  .person {
    position: absolute;
    left: 50px;
    top: 150px;
  }
  .person-name {
    color: var(--accent);
    font-weight: 600;
    font-size: 19px;
    line-height: 24px;
  }
  .person-title {
    color: var(--text-light);
    font-size: 15px;
    line-height: 20px;
  }
  .contact {
    position: absolute;
    left: 311px;
    top: 198px;
    color: var(--text-light);
    font-size: 15px;
    line-height: 20px;
  }
  .address { margin-bottom: 12px; }
  .contact-line {
    display: flex;
    align-items: center;
    gap: 5px;
  }
  .contact-line svg { width: 14px; height: 14px; flex: none; }
</style>
</head>
<body>
  <section class="card card-front" aria-label="Card front">
    <div class="front-pattern" role="img" aria-label="Repeating pattern of the company mark in shaded greys"></div>
    <div class="wordmark"><span class="wordmark-square"></span>Vornel Technologies</div>
  </section>

  <section class="card card-back" aria-label="Card back">
    <div class="back-decoration" role="img" aria-label="Large faint company mark decoration in brown and grey"></div>
    <div class="wordmark"><span class="wordmark-square"></span>Vornel Technologies</div>

    <span class="name-marker"></span>
    <div class="person">
      <p class="person-name">Daniel Hartley</p>
      <p class="person-title">President</p>
    </div>

    <div class="contact">
      <p class="address">418 Harbor Lane<br>Coral Point, Florida, 33190</p>
      <p class="contact-line">
        <svg viewBox="0 0 16 16" aria-hidden="true"><path d="M3 1.5l2.5 0 1 3.5-1.7 1.2a9 9 0 0 0 5 5l1.2-1.7 3.5 1v2.5c0 .8-.7 1.5-1.5 1.5A12.5 12.5 0 0 1 1.5 3c0-.8.7-1.5 1.5-1.5z" fill="var(--accent)"/></svg>
        (512) 555-0148
      </p>
      <p class="contact-line">
        <svg viewBox="0 0 16 16" aria-hidden="true"><rect x="1" y="3" width="14" height="10" fill="none" stroke="var(--accent)" stroke-width="1.6"/><path d="M1.5 3.5L8 9l6.5-5.5" fill="none" stroke="var(--accent)" stroke-width="1.6"/></svg>
        daniel@vorneltechnologies.com
      </p>
      <p class="contact-line">
        <svg viewBox="0 0 16 16" aria-hidden="true"><circle cx="8" cy="8" r="6.5" fill="none" stroke="var(--accent)" stroke-width="1.4"/><ellipse cx="8" cy="8" rx="2.8" ry="6.5" fill="none" stroke="var(--accent)" stroke-width="1.2"/><path d="M1.5 8h13M2.5 5h11M2.5 11h11" stroke="var(--accent)" stroke-width="1.1"/></svg>
        www.vorneltechnologies.com
      </p>
    </div>
  </section>
</body>
</html>
```